KORBALT

The business want a professional looking business card. We have a scetch we will add but want the extra upgrade, and would like more suggestions for variations of our business cards.

```html
<!DOCTYPE html>
<html lang="en">
<head>
<meta charset="UTF-8">
<title>KORBALT – Business Card</title>
<link href="https://fonts.googleapis.com/css2?family=Playfair+Display:wght@400;600;700&family=Poppins:wght@400&display=swap" rel="stylesheet">
<style>
  :root {
    --backdrop: #3b3b3c;
    --card: #1c1c1d;
    --gold: #d9b25a;
    --gold-deep: #c39a42;
  }
  * { margin: 0; padding: 0; box-sizing: border-box; }
  html, body { width: 1200px; height: 800px; overflow: hidden; }
  body {
    background: var(--backdrop);
    display: flex;
    align-items: center;
    justify-content: center;
    gap: 44px;
  }
  .card {
    position: relative;
    width: 520px;
    height: 297px;
    background: var(--card);
    color: var(--gold);
    overflow: hidden;
  }

  /* Front */
  .card-front {
    display: flex;
    flex-direction: column;
    align-items: center;
    justify-content: center;
  }
  .brand-mark {
    width: 58px;
    height: 58px;
    border-radius: 50%;
    background: var(--gold);
    margin-bottom: 26px;
  }
  .brand-name {
    font-family: 'Playfair Display', serif;
    font-weight: 400;
    font-size: 40px;
    letter-spacing: 0.2em;
    padding-left: 0.2em;
    line-height: 1;
  }
  .brand-tagline {
    font-family: 'Playfair Display', serif;
    font-weight: 400;
    font-size: 13px;
    letter-spacing: 0.55em;
    padding-left: 0.55em;
    margin-top: 12px;
  }

  /* Back */
  .rule {
    position: absolute;
    height: 1px;
    background: var(--gold-deep);
  }
  .rule-top { left: 230px; right: 22px; top: 40px; }
  .rule-header { left: 30px; width: 290px; top: 84px; }
  .company-header {
    position: absolute;
    left: 30px;
    top: 56px;
    font-family: 'Playfair Display', serif;
    font-weight: 700;
    font-size: 19px;
    letter-spacing: 0.01em;
  }
  .holder {
    position: absolute;
    left: 262px;
    top: 104px;
    font-family: 'Poppins', sans-serif;
  }
  .holder-name { font-size: 18px; line-height: 1.2; }
  .holder-role { font-size: 12px; margin-top: 2px; }

  .back-brand {
    position: absolute;
    left: 62px;
    top: 176px;
    display: flex;
    align-items: center;
    gap: 10px;
  }
  .back-brand .dot {
    width: 18px; height: 18px; border-radius: 50%; background: var(--gold);
  }
  .back-brand .word {
    font-family: 'Playfair Display', serif;
    font-weight: 400;
    font-size: 20px;
    letter-spacing: 0.14em;
  }

  .contact-list {
    position: absolute;
    left: 262px;
    top: 184px;
    list-style: none;
    font-family: 'Poppins', sans-serif;
    font-size: 12.5px;
  }
  .contact-list li {
    display: flex;
    align-items: center;
    gap: 10px;
    height: 22px;
  }
  .contact-list svg {
    width: 13px; height: 13px;
    fill: none; stroke: var(--gold); stroke-width: 1.6;
    stroke-linecap: round; stroke-linejoin: round;
  }
</style>
</head>
<body>

  <section class="card card-front" aria-label="Card front">
    <div class="brand-mark"></div>
    <div class="brand-name">KORBALT</div>
    <div class="brand-tagline">APPAREL</div>
  </section>

  <section class="card card-back" aria-label="Card back">
    <div class="rule rule-top"></div>
    <div class="company-header">KORBALT HAUGSTAD</div>
    <div class="rule rule-header"></div>

    <div class="holder">
      <div class="holder-name">Anders Lien Haugstad</div>
      <div class="holder-role">CEO &amp; Founder</div>
    </div>

    <div class="back-brand">
      <span class="dot"></span>
      <span class="word">KORBALT</span>
    </div>

    <ul class="contact-list">
      <li>
        <svg viewBox="0 0 16 16" aria-hidden="true"><rect x="4" y="1.5" width="8" height="13" rx="1.6"/><line x1="7" y1="12" x2="9" y2="12"/></svg>
        <span>004791234567</span>
      </li>
      <li>
        <svg viewBox="0 0 16 16" aria-hidden="true"><rect x="1.5" y="3.5" width="13" height="9" rx="1"/><polyline points="1.5,4 8,9 14.5,4"/></svg>
        <span>korbalt.llc@mailbox.no</span>
      </li>
      <li>
        <svg viewBox="0 0 16 16" aria-hidden="true"><circle cx="8" cy="8" r="6.5"/><ellipse cx="8" cy="8" rx="2.8" ry="6.5"/><line x1="1.5" y1="8" x2="14.5" y2="8"/></svg>
        <span>www.korbalt.llc</span>
      </li>
    </ul>
  </section>

</body>
</html>
```